Using attached logo that has been created

Business card with logo that's attached. Maybe with water or the cartoon van in background. Looking for it to not be so plain and not too white.
Information to include;
Dario Whitlock
(555) 208-7713
Info@mossbrookpipeworks.example
www.mossbrookpipeworks.example
License # 5320417
Looking forward to the designs u come up with.
Thank you!
-Teresa
The designer (Brynn), that I would like to work with requested an extension to allow time to create a couple designs for this project.
Target Market(s)
Plumbing
Industry/Entity Type
Plumbing
Contact Information for Business Card
Listed above
Font styles to use
Look and feel

```html
<!DOCTYPE html>
<html lang="en">
<head>
<meta charset="utf-8">
<title>Mossbrook Pipeworks – Business Card</title>
<link href="https://fonts.googleapis.com/css2?family=Arimo:wght@400;700&display=swap" rel="stylesheet">
<style>
  :root {
    --bg: #c9c9c9;
    --brand-blue: #0d55aa;
    --ink: #1d1d1d;
    --gold: #f2b311;
    --paper: #ffffff;
    --skin: #c98f6a;
    --khaki: #a88a5c;
  }
  * { margin: 0; padding: 0; box-sizing: border-box; }
  html, body {
    width: 1200px; height: 800px; overflow: hidden;
    background: var(--bg);
    font-family: "Arimo", Arial, sans-serif;
  }
  .canvas { position: relative; width: 1200px; height: 800px; }

  .card {
    position: absolute;
    width: 600px; height: 343px; left: 300px;
    box-shadow: 0 10px 24px rgba(0,0,0,.25);
    overflow: hidden;
  }
  .card--front { top: 40px; background: var(--paper); border-bottom: 3px solid var(--brand-blue); }
  .card--back { top: 417px; background: var(--brand-blue); }

  /* Front */
  .front-divider {
    position: absolute; left: 300px; top: 0; width: 1px; height: 100%;
    background: linear-gradient(to bottom, rgba(0,0,0,0), rgba(0,0,0,.08), rgba(0,0,0,0));
  }
  .mascot-small {
    position: absolute; left: 60px; top: 70px; width: 150px; height: 150px;
    border-radius: 6px;
    background: linear-gradient(160deg, var(--skin) 0%, var(--brand-blue) 45%, var(--khaki) 100%);
  }
  .brand-name--front {
    position: absolute; left: 40px; top: 236px; width: 200px;
    text-align: center;
    font-weight: 700; font-size: 22px; line-height: 1.1;
    color: var(--brand-blue); text-transform: uppercase;
  }
  .contact {
    position: absolute; left: 330px; top: 78px;
  }
  .contact__name {
    font-weight: 700; font-size: 24px; color: var(--brand-blue);
    text-transform: uppercase; letter-spacing: .5px; margin-bottom: 16px;
  }
  .contact__row {
    display: flex; align-items: center; gap: 8px;
    font-size: 13.5px; color: var(--ink); margin-bottom: 7px; white-space: nowrap;
  }
  .contact__row svg { width: 14px; height: 14px; flex: none; }
  .contact__license { margin-top: 16px; font-size: 15px; color: var(--brand-blue); }
  .contact__license span { color: var(--gold); }

  /* Back */
  .mascot-large {
    position: absolute; right: 40px; top: 30px; width: 230px; height: 313px;
    border-radius: 8px 8px 0 0;
    background: linear-gradient(170deg, var(--skin) 0%, #1f6fd0 40%, var(--khaki) 85%, var(--gold) 100%);
  }
  .brand-name--back {
    position: absolute; left: 56px; bottom: 62px;
    font-weight: 700; font-size: 40px; line-height: 1.05;
    color: var(--paper); text-transform: uppercase;
  }
</style>
</head>
<body>
<main class="canvas">

  <section class="card card--front">
    <div class="mascot-small" role="img" aria-label="Cartoon plumber mascot holding a pipe wrench and circular saw"></div>
    <p class="brand-name--front">Mossbrook Pipeworks</p>
    <div class="front-divider"></div>

    <div class="contact">
      <p class="contact__name">Dario Whitlock</p>
      <p class="contact__row">
        <svg viewBox="0 0 24 24" aria-hidden="true"><path fill="#0d55aa" d="M6.6 10.8a15 15 0 0 0 6.6 6.6l2.2-2.2a1 1 0 0 1 1-.25 11.4 11.4 0 0 0 3.6.57 1 1 0 0 1 1 1V20a1 1 0 0 1-1 1A17 17 0 0 1 3 4a1 1 0 0 1 1-1h3.5a1 1 0 0 1 1 1 11.4 11.4 0 0 0 .57 3.6 1 1 0 0 1-.25 1z"/></svg>
        (555) 208-7713
      </p>
      <p class="contact__row">
        <svg viewBox="0 0 24 24" aria-hidden="true"><rect x="2" y="5" width="20" height="14" fill="#0d55aa"/><path d="M2 5l10 8 10-8" fill="none" stroke="#fff" stroke-width="1.6"/></svg>
        Info@mossbrookpipeworks.example
      </p>
      <p class="contact__row">
        <svg viewBox="0 0 24 24" aria-hidden="true"><circle cx="12" cy="12" r="10" fill="#0d55aa"/><g fill="none" stroke="#fff" stroke-width="1.3"><ellipse cx="12" cy="12" rx="4" ry="10"/><path d="M2 12h20M4 7h16M4 17h16"/></g></svg>
        www.mossbrookpipeworks.example
      </p>
      <p class="contact__license">License <span># 5320417</span></p>
    </div>
  </section>

  <section class="card card--back">
    <p class="brand-name--back">Mossbrook<br>Pipeworks</p>
    <div class="mascot-large" role="img" aria-label="Large cartoon plumber mascot with a pipe wrench and circular saw"></div>
  </section>

</main>
</body>
</html>
```